"Kaleidoscope Journals" book cover design

PLEASE READ THE SHOULD NOT HAVES. DO NOT USE THE IMAGE I PROVIDED FOR THE KEYHOLE. I JUST PULLED THAT OFF SERCHLY TO SHOW AN EXAMPLE.

Front cover sketch is supposed to be a keyhole on a doorway. I’m picturing and older, more rustic/weathered wood and keyhole.

Hoping the back cover can be a reversed, mirror image of the front with an eye peeking through the exact same keyhole.

I don't have the book edited and formatted yet, but based on my other books' word and page count at 5.25x8, this one should come out to about 375 pages (to keep in mind for spine width).

Here is the back cover summary:

From awkward virgin to male entertainer to a spell of chastity, Kaleidoscope Journals traces a coming-of-age story fueled by the power of psychedelics. These tales tumble down a rabbit hole of life’s dualities—ranging from addiction to sobriety, philandering to celibacy, narcissism to spiritualism, and atheism to meeting God. Both the darkest corners of the human psyche and the lightest experiences of existential bliss are explored in this winding series. These musings highlight the wisdom gained from experimentation with LSD and Psilocybin.

Psychedelics are a trowel that digs deep into the soil of the soul, unearthing experiences beyond imagination. You hold in your hands a collection of the most important lessons learned by an explorer who delved into varying degrees of this otherworldly consciousness roughly a hundred times over five years. Whether these recollections were spiritual occurrences induced by a higher power or just convincing hallucinations brought on by a chemical power doesn’t matter. The trips were often more real than any occurrence on the sober plane of existence and pivotal in shaping one man’s worldview.

Target Market(s)

Community interested in psychedelics, mushrooms, LSD, spiritual healing, trauma healing, spiritual experience, etc.

Other font styles liked:
• Times New Roman for the back summary

Requirements
Must have
• 5.25x8, formatted for upload on Tolvex BPS
Nice to have
• I'm hoping the font for the title and “Anonymous” can look like someone carved them into the door, like you would names on a tree.
Should not have
• No AI generated images preferred. Also, the images I provided were pulled off Serchly for inspiration, but should not be used in your design.

```html
<!DOCTYPE html>
<html lang="en">
<head>
<meta charset="utf-8">
<title>Kaleidoscope Journals – Book Cover</title>
<link rel="stylesheet" href="https://fonts.googleapis.com/css2?family=Metamorphous&family=Tinos&display=swap">
<style>
  :root {
    --stage-grey: #c4c4c4;
    --wood-dark: #2e2118;
    --wood-mid: #5a4434;
    --wood-light: #7a6250;
    --carve: #e9cfa4;
    --carve-shadow: #6b4a2a;
    --gold-light: #f3dfae;
    --gold: #d2a55c;
    --gold-deep: #9d7236;
    --glow: #f8f3e6;
    --trip-pink: #e77fd0;
    --trip-violet: #5a3aa8;
    --trip-blue: #2f8fd8;
    --trip-night: #1b1f5c;
    --iris-blue: #2b9fd0;
    --lid-brown: #6d4a3a;
    --summary-ink: #ffffff;
    --ink-black: #000000;
  }
  * { box-sizing: border-box; margin: 0; padding: 0; }
  html, body { width: 1200px; height: 864px; overflow: hidden; }
  body { background: var(--stage-grey); position: relative; }

  .cover {
    position: absolute;
    top: 88px;
    width: 451px;
    height: 688px;
    overflow: hidden;
  }
  .cover--front { left: 106px; }
  .cover--back { left: 643px; }

  .wood {
    position: absolute; inset: 0;
    background:
      repeating-linear-gradient(90deg, rgba(0,0,0,0.18) 0 2px, transparent 2px 23px, rgba(255,255,255,0.05) 23px 25px, transparent 25px 47px),
      linear-gradient(90deg, var(--wood-dark), var(--wood-mid) 30%, var(--wood-light) 55%, var(--wood-mid) 80%, var(--wood-dark));
  }
  .cover--back .wood::after {
    content: ""; position: absolute; inset: 0;
    background: linear-gradient(180deg, transparent 0%, transparent 38%, rgba(0,0,0,0.55) 62%, var(--ink-black) 82%);
  }

  .carved {
    position: absolute; left: 12px; right: 12px;
    text-align: center;
    font-family: "Metamorphous", serif;
    font-weight: 400;
    color: var(--carve);
    text-shadow: 1px 1px 0 var(--carve-shadow), -1px -1px 0 rgba(0,0,0,0.35);
    text-transform: uppercase;
    white-space: nowrap;
  }
  .cover-title { top: 22px; font-size: 25px; line-height: 32px; letter-spacing: 0; }
  .cover-author { top: 614px; font-size: 48px; line-height: 56px; letter-spacing: 1px; }

  .keyhole-plate { position: absolute; }
  .cover--front .keyhole-plate { left: 37px; top: 81px; width: 376px; height: 524px; }
  .cover--back .keyhole-plate { left: 140px; top: 37px; width: 175px; height: 243px; }

  .summary {
    position: absolute;
    left: 30px; right: 30px; top: 306px;
    font-family: "Tinos", "Times New Roman", serif;
    font-size: 12.2px;
    line-height: 15.5px;
    color: var(--summary-ink);
    text-align: center;
  }
  .summary p + p { margin-top: 15px; }
</style>
</head>
<body>

<section class="cover cover--front" aria-label="Front cover">
  <div class="wood" role="img" aria-label="Weathered dark wood door texture"></div>

  <svg class="keyhole-plate" viewBox="0 0 376 524">
    <defs>
      <linearGradient id="front-gold" x1="0" y1="0" x2="1" y2="1">
        <stop offset="0" stop-color="var(--gold-light)"/>
        <stop offset="0.5" stop-color="var(--gold)"/>
        <stop offset="1" stop-color="var(--gold-deep)"/>
      </linearGradient>
      <linearGradient id="front-scene" x1="0" y1="0" x2="0" y2="1">
        <stop offset="0" stop-color="var(--trip-night)"/>
        <stop offset="0.3" stop-color="var(--trip-pink)"/>
        <stop offset="0.55" stop-color="var(--trip-violet)"/>
        <stop offset="1" stop-color="var(--trip-blue)"/>
      </linearGradient>
    </defs>
    <path class="plate-frame" d="M0 188 A188 188 0 0 1 376 188 V470 A54 54 0 0 1 322 524 H54 A54 54 0 0 1 0 470 Z" fill="url(#front-gold)"/>
    <path class="plate-inset" d="M40 196 A148 148 0 0 1 336 196 V458 A30 30 0 0 1 306 488 H70 A30 30 0 0 1 40 458 Z" fill="var(--glow)" opacity="0.85"/>
    <path class="keyhole-opening" role="img" aria-label="Illustration of a glowing psychedelic mushroom forest with a lone walker, seen through the keyhole"
      d="M143 346 A100 100 0 1 1 238 346 L299 447 H76 Z" fill="url(#front-scene)"/>
  </svg>

  <h1 class="carved cover-title">Kaleidoscope Journals</h1>
  <p class="carved cover-author">Anonymous</p>
</section>

<section class="cover cover--back" aria-label="Back cover">
  <div class="wood" role="img" aria-label="Weathered dark wood door texture fading to black"></div>

  <svg class="keyhole-plate" viewBox="0 0 175 243">
    <defs>
      <linearGradient id="back-gold" x1="0" y1="0" x2="1" y2="1">
        <stop offset="0" stop-color="var(--gold-light)"/>
        <stop offset="0.5" stop-color="var(--gold)"/>
        <stop offset="1" stop-color="var(--gold-deep)"/>
      </linearGradient>
      <radialGradient id="back-eye" cx="0.5" cy="0.35" r="0.6">
        <stop offset="0" stop-color="var(--iris-blue)"/>
        <stop offset="0.45" stop-color="var(--lid-brown)"/>
        <stop offset="1" stop-color="var(--wood-dark)"/>
      </radialGradient>
    </defs>
    <path class="plate-frame" d="M0 70 A70 70 0 0 1 70 0 H105 A70 70 0 0 1 175 70 V195 A48 48 0 0 1 127 243 H48 A48 48 0 0 1 0 195 Z" fill="url(#back-gold)"/>
    <path class="plate-inset" d="M18 78 A58 58 0 0 1 76 20 H99 A58 58 0 0 1 157 78 V190 A32 32 0 0 1 125 222 H50 A32 32 0 0 1 18 190 Z" fill="var(--glow)" opacity="0.8"/>
    <path class="keyhole-opening" role="img" aria-label="Photograph of an eye peering through the keyhole"
      d="M66 124 A45 45 0 1 1 107 124 L115 209 H60 Z" fill="url(#back-eye)"/>
  </svg>

  <div class="summary">
    <p>From awkward virgin to male entertainer to a spell of chastity, Kaleidoscope Journals traces a coming-of-age story fueled by the power of psychedelics. These tales tumble down a rabbit hole of life’s dualities—ranging from addiction to sobriety, philandering to celibacy, narcissism to spiritualism, and atheism to meeting God. Both the darkest corners of the human psyche and the lightest experiences of existential bliss are explored in this winding series. These musings highlight the wisdom gained from experimentation with LSD and Psilocybin.</p>
    <p>Psychedelics are a trowel that digs deep into the soil of the soul, unearthing experiences beyond imagination. You hold in your hands a collection of the most important lessons learned by an explorer who delved into varying degrees of this otherworldly consciousness roughly a hundred times over five years. Whether these recollections were spiritual occurrences induced by a higher power or just convincing hallucinations brought on by a chemical power doesn’t matter. The trips were often more real than any occurrence on the sober plane of existence and pivotal in shaping one man’s worldview.</p>
  </div>
</section>

</body>
</html>
```